Realty Group Needs Classy, Contemporary Letterhead Design

We need a letterhead design for a new realty company located in NY, USA. We buy investment properties to rehabilitate and or keep in our rental portfolio.

```html
<!DOCTYPE html>
<html lang="en">
<head>
<meta charset="utf-8">
<title>Meridian Realty Group – Letterhead</title>
<link rel="stylesheet" href="https://fonts.googleapis.com/css2?family=Montserrat:wght@800&family=Roboto:wght@400&display=swap">
<style>
  :root {
    --backdrop: #e7e7e7;
    --paper: #ffffff;
    --brand-purple: #522d84;
    --edge-grey: #7f7f7f;
    --text-grey: #666666;
    --tint-light: #f8f8fb;
    --tint-deep: #efedf5;
  }
  html, body {
    margin: 0;
    padding: 0;
    width: 1023px;
    height: 1200px;
    overflow: hidden;
    background: var(--backdrop);
  }
  .letterhead {
    position: absolute;
    left: 115px;
    top: 40px;
    width: 793px;
    height: 1120px;
    background: var(--paper);
    overflow: hidden;
  }
  .edge-bar {
    position: absolute;
    left: 0;
    top: 0;
    width: 16px;
    height: 100%;
    background: var(--edge-grey);
  }
  .side-band {
    position: absolute;
    left: 717px;
    top: 0;
    width: 76px;
    height: 100%;
  }
  .brand {
    position: absolute;
    left: 55px;
    top: 72px;
    display: flex;
    align-items: center;
    gap: 10px;
  }
  .brand-mark {
    width: 14px;
    height: 14px;
    background: var(--brand-purple);
  }
  .brand-name {
    font-family: "Montserrat", sans-serif;
    font-weight: 800;
    font-size: 22px;
    letter-spacing: -0.3px;
    color: var(--brand-purple);
  }
  .contact-list {
    position: absolute;
    right: 106px;
    top: 50px;
    margin: 0;
    padding: 0;
    list-style: none;
  }
  .contact-item {
    display: flex;
    justify-content: flex-end;
    align-items: center;
    gap: 12px;
    height: 24.5px;
    font-family: "Roboto", sans-serif;
    font-size: 11.5px;
    color: var(--text-grey);
  }
  .contact-icon {
    width: 14px;
    height: 14px;
    fill: var(--brand-purple);
  }
  .watermark {
    position: absolute;
    left: 16px;
    top: 358px;
    width: 688px;
    height: 762px;
    background: linear-gradient(90deg, var(--tint-light), var(--tint-deep));
    border-radius: 0 260px 0 0;
  }
</style>
</head>
<body>
  <main class="letterhead">
    <div class="edge-bar"></div>

    <div class="watermark" role="img" aria-label="Faint oversized brand emblem watermark in pale lavender"></div>

    <header class="brand">
      <span class="brand-mark"></span>
      <span class="brand-name">Meridian Realty Group</span>
    </header>

    <ul class="contact-list">
      <li class="contact-item">
        <span>0123 Zip,abc City</span>
        <svg class="contact-icon" viewBox="0 0 24 24" aria-hidden="true"><path d="M12 2a7 7 0 0 0-7 7c0 5.2 7 13 7 13s7-7.8 7-13a7 7 0 0 0-7-7zm0 9.5A2.5 2.5 0 1 1 12 6.5a2.5 2.5 0 0 1 0 5z"/></svg>
      </li>
      <li class="contact-item">
        <span>+00 1234 56 789</span>
        <svg class="contact-icon" viewBox="0 0 24 24" aria-hidden="true"><path d="M6.6 10.8a15.1 15.1 0 0 0 6.6 6.6l2.2-2.2a1 1 0 0 1 1-.25 11.4 11.4 0 0 0 3.6.57 1 1 0 0 1 1 1V20a1 1 0 0 1-1 1A17 17 0 0 1 3 4a1 1 0 0 1 1-1h3.5a1 1 0 0 1 1 1c0 1.25.2 2.45.57 3.57a1 1 0 0 1-.25 1z"/></svg>
      </li>
      <li class="contact-item">
        <span>info@company.com</span>
        <svg class="contact-icon" viewBox="0 0 24 24" aria-hidden="true"><path d="M22 2 2 10.5l7 2.5 2.5 7z M9 13l13-11-9 14z"/></svg>
      </li>
    </ul>

    <svg class="side-band" viewBox="0 0 76 1120" preserveAspectRatio="none" aria-hidden="true">
      <defs>
        <linearGradient id="stripe-shine" x1="0" x2="1" y1="0" y2="0">
          <stop offset="0" stop-color="#8f6fc0"/>
          <stop offset="0.5" stop-color="#ffffff"/>
          <stop offset="1" stop-color="#8f6fc0"/>
        </linearGradient>
      </defs>
      <rect width="76" height="1120" fill="var(--brand-purple)"/>
      <rect x="6" y="780" width="3.5" height="340" fill="url(#stripe-shine)"/>
      <rect x="17" y="665" width="3.5" height="455" fill="url(#stripe-shine)"/>
      <rect x="29" y="559" width="3.5" height="561" fill="url(#stripe-shine)"/>
      <rect x="41" y="440" width="3.5" height="680" fill="url(#stripe-shine)"/>
      <rect x="53" y="208" width="3.5" height="912" fill="url(#stripe-shine)"/>
      <rect x="65" y="0" width="3.5" height="1120" fill="url(#stripe-shine)"/>
      <rect x="72.5" y="0" width="3.5" height="1120" fill="url(#stripe-shine)"/>
    </svg>
  </main>
</body>
</html>
```